Valemont Analysis Bureau Card Design

I need a business card for the agency I currently am tasked with, which is based in Hartford, CT. VMAB provides, disseminates and obtains intelligence in regards to ongoing criminal investigations throughout the State of CT. The information we obtain and provide, comes to us and is sent out by various Law Enforcement agencies throughout CT.

Industry/Entity Type

Business

Contact Information for Business Card

Officer Dale P. Ostrander
Halvick Police Department - Eastern Region Intelligence Officer
Valemont Analysis Bureau
2482 Harrow Mill Rd., Middletown, CT 06457
Work Cell: (860) 555-0147
E-Mail: vmab.er@halvorne-net.org

```html
<!DOCTYPE html>
<html lang="en">
<head>
<meta charset="utf-8">
<title>Halvick Police Business Card</title>
<link rel="stylesheet" href="https://fonts.googleapis.com/css2?family=Oswald:wght@500;600&family=Montserrat:wght@400;500&display=swap">
<style>
  :root {
    --backdrop: #d9d9db;
    --card-white: #ffffff;
    --brand-red: #c8192c;
    --accent-yellow: #f2d024;
    --ink: #1b1b1b;
    --on-red: #ffffff;
  }
  * { box-sizing: border-box; margin: 0; padding: 0; }
  html, body { width: 1200px; height: 988px; overflow: hidden; }
  body {
    background: var(--backdrop);
    font-family: "Montserrat", Arial, sans-serif;
    display: flex;
    flex-direction: column;
    align-items: center;
    justify-content: center;
    gap: 40px;
  }
  .card {
    position: relative;
    width: 760px;
    height: 434px;
    background: var(--card-white);
    box-shadow: 0 10px 28px rgba(0,0,0,0.18);
    overflow: hidden;
  }
  .card-art { position: absolute; inset: 0; width: 100%; height: 100%; }
  .agency-mark {
    position: absolute;
    display: flex;
    align-items: center;
    gap: 10px;
    font-family: "Oswald", Arial, sans-serif;
    font-weight: 600;
    font-size: 26px;
    letter-spacing: 1px;
    text-transform: uppercase;
    color: var(--ink);
    white-space: nowrap;
  }
  .agency-mark .dot {
    width: 22px; height: 22px; border-radius: 50%;
    background: var(--brand-red);
  }
  .card-back .agency-mark { left: 70px; top: 70px; }
  .card-front .agency-mark { left: 120px; bottom: 42px; }

  .identity {
    position: absolute;
    left: 60px; top: 140px;
    color: var(--on-red);
    white-space: nowrap;
  }
  .identity .name {
    font-family: "Oswald", Arial, sans-serif;
    font-weight: 500;
    font-size: 34px;
    letter-spacing: 1px;
    text-transform: uppercase;
    line-height: 1.1;
  }
  .identity .role {
    font-size: 11px;
    letter-spacing: 1px;
    text-transform: uppercase;
    margin-top: 4px;
  }
  .contact {
    position: absolute;
    list-style: none;
    color: var(--on-red);
    font-size: 12px;
    white-space: nowrap;
  }
  .contact li { display: flex; align-items: center; gap: 10px; height: 30px; }
  .contact svg { width: 20px; height: 20px; flex: none; }
  .contact-left { left: 60px; top: 212px; }
  .contact-right { left: 400px; top: 140px; }
</style>
</head>
<body>

  <section class="card card-back">
    <svg class="card-art" viewBox="0 0 760 434" preserveAspectRatio="none" aria-hidden="true">
      <polygon points="0,60 0,0 120,0" fill="var(--accent-yellow)"/>
      <polygon points="0,228 420,228 470,180 760,180 760,434 0,434" fill="var(--brand-red)"/>
      <polygon points="0,222 418,222 468,174 760,174 760,180 470,180 420,228 0,228" fill="var(--accent-yellow)"/>
    </svg>
    <div class="agency-mark"><span class="dot"></span>Halvick Police</div>
  </section>

  <section class="card card-front">
    <svg class="card-art" viewBox="0 0 760 434" preserveAspectRatio="none" aria-hidden="true">
      <polygon points="560,0 760,0 760,40 600,40" fill="var(--accent-yellow)"/>
      <polygon points="0,120 300,120 340,46 760,46 760,250 0,330" fill="var(--brand-red)"/>
      <polygon points="0,330 760,250 760,258 0,338" fill="var(--accent-yellow)"/>
      <polygon points="0,434 0,370 90,434" fill="var(--accent-yellow)"/>
    </svg>

    <div class="identity">
      <div class="name">Dale P. Ostrander</div>
      <div class="role">Eastern Region Intelligence Officer</div>
    </div>

    <ul class="contact contact-left">
      <li>
        <svg viewBox="0 0 20 20"><circle cx="10" cy="10" r="9" fill="none" stroke="currentColor" stroke-width="1.4"/><path d="M7 5.5l2 2-1 1.3c.6 1.3 1.5 2.2 2.8 2.8l1.3-1 2 2-1.2 1.3C9.8 13.5 6.5 10.2 6 7z" fill="currentColor"/></svg>
        Work Cell: (860) 555-0147
      </li>
      <li>
        <svg viewBox="0 0 20 20"><circle cx="10" cy="10" r="9" fill="none" stroke="currentColor" stroke-width="1.4"/><rect x="5" y="6.5" width="10" height="7" fill="none" stroke="currentColor" stroke-width="1.2"/><path d="M5 6.5l5 4 5-4" fill="none" stroke="currentColor" stroke-width="1.2"/></svg>
        vmab.er@halvorne-net.org
      </li>
    </ul>

    <ul class="contact contact-right">
      <li>
        <svg viewBox="0 0 20 20"><circle cx="10" cy="10" r="9" fill="none" stroke="currentColor" stroke-width="1.4"/><path d="M5.5 14.5h9M6.5 14.5V9M10 14.5V9M13.5 14.5V9M5.5 8.5L10 5.5l4.5 3z" fill="none" stroke="currentColor" stroke-width="1.2"/></svg>
        Valemont Analysis Bureau
      </li>
      <li>
        <svg viewBox="0 0 20 20"><circle cx="10" cy="10" r="9" fill="none" stroke="currentColor" stroke-width="1.4"/><path d="M5.5 14.5h9M6.5 14.5V9M10 14.5V9M13.5 14.5V9M5.5 8.5L10 5.5l4.5 3z" fill="none" stroke="currentColor" stroke-width="1.2"/></svg>
        Halvick Police Department
      </li>
      <li>
        <svg viewBox="0 0 20 20"><circle cx="10" cy="10" r="9" fill="none" stroke="currentColor" stroke-width="1.4"/><path d="M10 4.5a3.5 3.5 0 0 0-3.5 3.5c0 2.6 3.5 7 3.5 7s3.5-4.4 3.5-7A3.5 3.5 0 0 0 10 4.5zm0 4.8a1.3 1.3 0 1 1 0-2.6 1.3 1.3 0 0 1 0 2.6z" fill="currentColor"/></svg>
        2482 Harrow Mill Rd., Middletown, CT 06457
      </li>
    </ul>

    <div class="agency-mark"><span class="dot"></span>Halvick Police</div>
  </section>

</body>
</html>
```